HVAC Door Hanger- 4.25 inches by 11 inches

Hello We are using the Brightvale door hanger as an inspiration for our new door hanger. The company name is Corvant Home Services. Logo files attached. The Slogan needs to be added on the front with the Logo "Southern California’s Trusted Name in Home Services". Instead of the X protection plan, the name will be Full Shield by Corvant or Corvant Climate Keeper- The slogan for this package will be "Peace of Mind, For Every Season

```html
<!DOCTYPE html>
<html lang="en">
<head>
<meta charset="utf-8">
<title>Corvant Home Services – Door Hanger</title>
<link href="https://fonts.googleapis.com/css2?family=Fredoka:wght@500;600;700&family=Poppins:wght@400;500;600;700;800&display=swap" rel="stylesheet">
<style>
  :root {
    --stage: #585858;
    --hole: #5a5a5a;
    --sky-light: #ffffff;
    --sky: #d6ecf8;
    --brand-blue: #1573ac;
    --orange: #f39a1e;
    --red: #e41e26;
    --yellow: #f7d21c;
    --ink: #1a1a1a;
    --white: #ffffff;
  }
  * { box-sizing: border-box; margin: 0; padding: 0; }
  html, body { width: 1191px; height: 1200px; overflow: hidden; }
  body { background: var(--stage); position: relative; font-family: "Poppins", sans-serif; }

  .hanger {
    position: absolute; top: 142px; width: 354px; height: 916px; overflow: hidden;
    background: radial-gradient(ellipse at 50% 45%, var(--sky-light) 35%, var(--sky) 100%);
    box-shadow: 0 4px 14px rgba(0,0,0,.35);
  }
  .hanger--front { left: 168px; }
  .hanger--back { left: 670px; }

  .hanger__shapes { position: absolute; inset: 0; width: 354px; height: 916px; }

  .abs { position: absolute; left: 0; width: 100%; text-align: center; white-space: nowrap; }

  /* Front */
  .brand { top: 240px; left: 36px; width: 282px; text-align: left; }
  .brand__name { display: flex; align-items: center; gap: 8px; font-family: "Fredoka", sans-serif; font-weight: 600; font-size: 34px; color: var(--brand-blue); line-height: 1; }
  .brand__mark { width: 16px; height: 16px; background: var(--orange); border-radius: 50%; flex: none; }
  .brand__sub { margin-top: 2px; font-size: 10px; font-weight: 500; letter-spacing: 8.2px; color: var(--orange); line-height: 12px; }
  .brand__trades { margin-top: 2px; font-size: 9.2px; font-weight: 600; letter-spacing: 1.3px; color: var(--red); }

  .slogan-bar { top: 319px; left: 36px; width: 282px; height: 32px; background: var(--orange); color: var(--white);
    font-family: "Fredoka", sans-serif; font-weight: 600; font-size: 21px; line-height: 32px; }
  .slogan-line { top: 352px; font-family: "Fredoka", sans-serif; font-weight: 700; font-size: 24px; color: var(--red); line-height: 30px; }
  .headline { top: 392px; font-family: "Poppins", sans-serif; font-weight: 800; font-size: 55px; line-height: 52px; color: var(--brand-blue); letter-spacing: -1.5px; }

  .phone { top: 797px; display: flex; justify-content: center; align-items: center; gap: 8px;
    font-family: "Fredoka", sans-serif; font-weight: 700; font-size: 40px; color: var(--white); line-height: 44px; }
  .phone__icon { width: 26px; height: 26px; flex: none; }
  .web { top: 851px; left: 36px; width: 282px; height: 29px; border-radius: 15px; background: var(--red); color: var(--white);
    font-family: "Poppins", sans-serif; font-weight: 500; font-size: 20px; letter-spacing: 1.4px; line-height: 29px; }

  /* Back */
  .tagline { top: 204px; font-family: "Fredoka", sans-serif; font-weight: 700; font-size: 21px; line-height: 21px; color: var(--orange); }
  .reduced { top: 250px; font-size: 12.5px; font-weight: 600; color: var(--ink); line-height: 17px; }
  .reduced b { color: var(--brand-blue); font-weight: 700; }
  .reduced sup { font-size: 7px; }

  .offer { position: absolute; top: 307px; left: 36px; width: 291px; height: 134px; border-radius: 8px; overflow: hidden;
    display: flex; box-shadow: 0 2px 5px rgba(0,0,0,.25); }
  .offer__main { width: 196px; background: var(--brand-blue); padding: 10px 0 0 15px; color: var(--white); }
  .offer__title { font-family: "Fredoka", sans-serif; font-weight: 700; font-size: 17px; color: var(--yellow); line-height: 18px; }
  .offer__price { font-family: "Fredoka", sans-serif; font-weight: 500; font-size: 36px; line-height: 40px; margin-left: 10px; }
  .offer__price sup { font-size: 16px; vertical-align: 14px; }
  .offer__items { display: grid; grid-template-columns: 1fr 1fr; gap: 2px 6px; margin-top: 4px; font-size: 6.2px; line-height: 7.5px; }
  .offer__items li { list-style: none; position: relative; padding-left: 8px; }
  .offer__items li::before { content: ""; position: absolute; left: 0; top: 1.5px; width: 4.5px; height: 4.5px; border-radius: 50%; background: var(--yellow); }
  .offer__rebate { margin-top: 8px; font-size: 7px; font-weight: 600; color: var(--yellow); white-space: nowrap; }
  .offer__stripe { width: 6px; background: var(--yellow); }
  .offer__reg { flex: 1; background: var(--red); color: var(--white); font-family: "Fredoka", sans-serif; font-weight: 600;
    font-size: 30px; line-height: 33px; text-align: center; padding-top: 50px; }
  .offer__reg sup { font-size: 14px; vertical-align: 12px; }
  .badge { position: absolute; top: 286px; left: 254px; width: 64px; height: 64px; }

  .plan-heading { top: 455px; display: flex; align-items: center; justify-content: center; gap: 8px;
    font-family: "Fredoka", sans-serif; font-weight: 700; font-size: 17px; color: var(--orange); line-height: 22px; }
  .plan-heading::before, .plan-heading::after { content: ""; width: 34px; height: 1px; background: #777; }
  .plan-list { position: absolute; top: 491px; left: 36px; width: 290px; display: grid; grid-template-columns: 167px 1fr;
    font-size: 8.6px; line-height: 10.5px; color: var(--ink); }
  .plan-list ul { list-style: none; display: flex; flex-direction: column; gap: 7px; }
  .plan-list li { position: relative; padding-left: 13px; }
  .plan-list li::before { content: ""; position: absolute; left: 0; top: 1.5px; width: 7px; height: 7px; border-radius: 50%; background: var(--brand-blue); }
</style>
</head>
<body>

<section class="hanger hanger--front" aria-label="Door hanger front">
  <svg class="hanger__shapes" viewBox="0 0 354 916">
    <defs>
      <linearGradient id="photoFront" x1="0" y1="0" x2="1" y2="1">
        <stop offset="0" stop-color="#b7b3ad"/><stop offset=".5" stop-color="#3d4650"/><stop offset="1" stop-color="#25466e"/>
      </linearGradient>
    </defs>
    <line x1="57" y1="0" x2="140" y2="76" stroke="var(--hole)" stroke-width="6"/>
    <circle cx="175" cy="120" r="64" fill="var(--hole)"/>
    <polygon points="0,640 184,740 354,635 354,916 0,916" fill="var(--brand-blue)"/>
    <polygon points="183,511 306,582 306,712 183,783 60,712 60,582" fill="var(--white)"/>
    <polygon role="img" aria-label="Photo of a technician in a hard hat servicing an outdoor air conditioning unit" points="183,518 301,586 301,708 183,776 65,708 65,586" fill="url(#photoFront)"/>
    <polyline points="60,700 60,582 183,511 306,582 306,640" fill="none" stroke="var(--red)" stroke-width="2"/>
  </svg>

  <div class="abs brand">
    <div class="brand__name"><span>CORVANT</span><span class="brand__mark"></span></div>
    <div class="brand__sub">HOME SERVICES</div>
    <div class="brand__trades">HEATING COOLING PLUMBING ELECTRICAL</div>
  </div>

  <div class="abs slogan-bar">SOUTHERN CALIFORNIA’S</div>
  <div class="abs slogan-line">TRUSTED NAME IN</div>
  <h1 class="abs headline">HOME<br>SERVICES</h1>

  <div class="abs phone">
    <svg class="phone__icon" viewBox="0 0 26 26"><circle cx="13" cy="13" r="13" fill="var(--orange)"/><path d="M9 7c1 0 2 2.5 2 3.2s-1.2 1.1-1 1.8c.6 1.8 2 3.2 3.8 3.9.7.2 1.1-1 1.8-1s3.2 1 3.2 2-1.4 2.3-2.6 2.3C11 19.2 6.8 15 6.8 9.6 6.8 8.4 8 7 9 7z" fill="var(--white)"/></svg>
    <span>5550184270</span>
  </div>
  <div class="abs web">www.corvanthome.com</div>
</section>

<section class="hanger hanger--back" aria-label="Door hanger back">
  <svg class="hanger__shapes" viewBox="0 0 354 916">
    <defs>
      <linearGradient id="photoBack" x1="0" y1="0" x2="1" y2="1">
        <stop offset="0" stop-color="#d8d2c8"/><stop offset=".5" stop-color="#4a5560"/><stop offset="1" stop-color="#2f6fa8"/>
      </linearGradient>
    </defs>
    <line x1="57" y1="0" x2="140" y2="76" stroke="var(--hole)" stroke-width="6"/>
    <circle cx="175" cy="120" r="64" fill="var(--hole)"/>
    <polygon points="0,634 180,730 354,634 354,916 0,916" fill="var(--brand-blue)"/>
    <polygon points="177,582 272,637 272,732 177,787 82,732 82,637" fill="var(--white)"/>
    <polygon role="img" aria-label="Photo of a technician checking refrigerant gauges on an air conditioning unit" points="177,588 267,640 267,729 177,781 87,729 87,640" fill="url(#photoBack)"/>
    <polyline points="82,690 82,637 177,582 272,637 272,690" fill="none" stroke="var(--red)" stroke-width="2"/>
  </svg>

  <h2 class="abs tagline">PEACE OF MIND<br>FOR EVERY SEASON</h2>
  <p class="abs reduced">Monthly Service Reduced<br>From <b><sup>$</sup>29.99/Month</b> to <b><sup>$</sup>19.99/Month</b></p>

  <div class="offer">
    <div class="offer__main">
      <div class="offer__title">HALF OFF SPECIAL!</div>
      <div class="offer__price">ONLY <sup>$</sup>88</div>
      <ul class="offer__items">
        <li>A/C System Safety Inspection + Tune-Up</li>
        <li>Whole Home Water Safety Inspection</li>
        <li>Standard Water Heater Flush</li>
        <li>Accessible Drain Cleaning</li>
      </ul>
      <div class="offer__rebate">Get up to $10,000 in State &amp; Federal Rebates!!!</div>
    </div>
    <div class="offer__stripe"></div>
    <div class="offer__reg">REG<br><sup>$</sup>172</div>
  </div>
  <svg class="badge" viewBox="0 0 64 64" aria-label="Limited time offer">
    <circle cx="32" cy="32" r="30" fill="var(--yellow)"/>
    <circle cx="32" cy="32" r="26" fill="none" stroke="var(--white)" stroke-width="1" stroke-dasharray="2 2"/>
    <text x="32" y="24" text-anchor="middle" font-family="Fredoka, sans-serif" font-weight="700" font-size="10" fill="var(--red)">LIMITED</text>
    <text x="32" y="35" text-anchor="middle" font-family="Fredoka, sans-serif" font-weight="700" font-size="10" fill="var(--red)">TIME</text>
    <text x="32" y="46" text-anchor="middle" font-family="Fredoka, sans-serif" font-weight="700" font-size="10" fill="var(--red)">OFFER</text>
  </svg>

  <h3 class="abs plan-heading">CORVANT CLIMATE KEEPER</h3>
  <div class="plan-list">
    <ul>
      <li>One X Performance<br>Heating Tune-up per year</li>
      <li>One X Performance A/C<br>Tune-up per year</li>
      <li>10% Off In-Door Air Quality<br>Products</li>
    </ul>
    <ul>
      <li>One Water Heater Flush<br>per year</li>
      <li>Priority Installation</li>
      <li>Transferrable Plan AND<br>MUCH MORE</li>
    </ul>
  </div>

  <div class="abs phone">
    <svg class="phone__icon" viewBox="0 0 26 26"><circle cx="13" cy="13" r="13" fill="var(--orange)"/><path d="M9 7c1 0 2 2.5 2 3.2s-1.2 1.1-1 1.8c.6 1.8 2 3.2 3.8 3.9.7.2 1.1-1 1.8-1s3.2 1 3.2 2-1.4 2.3-2.6 2.3C11 19.2 6.8 15 6.8 9.6 6.8 8.4 8 7 9 7z" fill="var(--white)"/></svg>
    <span>5550184270</span>
  </div>
  <div class="abs web">www.corvanthome.com</div>
</section>

</body>
</html>
```